We need a design for a contracting company website based in KSA, something modern with the same color theme as the attached logo. including a page for people who want to submit their CV and try to apply for a job.Also to include the "about us, contact us, gallery, Divisions, Supplies, etc...". If possible to have an interactive or moving background. Please disregard the "Bright Pathways" Section in the attached profile.

Industry/Entity Type

Construction Company

Number of Pages Required

5+ page

Colors

Designer to choose colors to be used in the design.

Requirements
Must have
• Pages:
• about us, contact us, gallery, Divisions, Apply for a job, Supplies
Nice to have
• - Moving or interactive background

```html
<!DOCTYPE html>
<html lang="en">
<head>
<meta charset="utf-8">
<title>About Us – Cobaltine Building Company</title>
<link rel="stylesheet" href="https://fonts.googleapis.com/css2?family=Montserrat:wght@600;700;800&family=Lato:wght@400&display=swap">
<style>
:root{
  --orange:#f2a020;
  --dark:#1a0f0b;
  --brown:#3d2816;
  --ink:#222;
  --body:#4a4a4a;
  --white:#fff;
  --head:'Montserrat',sans-serif;
  --text:'Lato',sans-serif;
}
*{margin:0;padding:0;box-sizing:border-box}
html,body{width:1200px;height:2270px;overflow:hidden;background:var(--white)}
.page{position:relative;width:1200px;height:2270px;overflow:hidden;font-family:var(--text);color:var(--body)}
.abs{position:absolute}

/* header */
.call-bar{left:709px;top:0;width:491px;height:50px;background:var(--orange);clip-path:polygon(0 0,100% 0,100% 100%,60px 100%);
  color:var(--white);font:700 17px var(--head);display:flex;align-items:center;padding-left:62px;gap:7px}
.call-bar svg{width:18px;height:18px}
.brand{left:139px;top:62px;display:flex;align-items:center;gap:10px}
.brand-mark{width:52px;height:52px;background:var(--orange)}
.brand-name{font:700 17px var(--head);color:var(--ink);line-height:1.2;width:190px}
.nav{left:422px;top:81px;display:flex;font:700 14px var(--head);color:var(--ink)}
.nav a{position:absolute;white-space:nowrap;color:inherit;text-decoration:none}
.nav a.active{color:var(--orange)}
.nav a.active::after{content:"";position:absolute;left:0;right:0;bottom:-9px;height:2px;background:var(--orange)}

/* hero */
.hero{left:0;top:134px;width:1200px;height:428px}
.hero-photo{position:absolute;inset:0;background:linear-gradient(180deg,#2d4566 0%,#4d6a8c 45%,#5a6878 75%,#3b4552 100%)}
.hero h1{position:absolute;left:0;right:28px;top:170px;text-align:center;font:800 46px var(--head);color:var(--white)}
.hero svg{position:absolute;inset:0}

/* about */
.about-frame{background:var(--orange)}
.about-photo{left:176px;top:654px;width:333px;height:305px;background:linear-gradient(160deg,#3b4a7a 0%,#3a3660 40%,#7a4a5e 75%,#c08050 100%)}
.about-title{left:571px;top:630px;font:800 33px var(--head);color:var(--ink)}
.about-copy{left:574px;top:688px;width:500px;font-size:17px;line-height:27px}
.about-copy p+p{margin-top:30px}

/* why choose */
.why{left:0;top:1075px;width:1200px;height:425px}
.why h2{position:absolute;left:0;right:10px;top:76px;text-align:center;font:800 28px var(--head);color:var(--white)}
.feature{position:absolute;top:157px;width:300px;height:115px}
.feature .hex{position:absolute;left:0;top:0;width:100px;height:114px;background:var(--orange);
  clip-path:polygon(50% 0,100% 25%,100% 75%,50% 100%,0 75%,0 25%);display:flex;align-items:center;justify-content:center}
.feature .hex svg{width:56px;height:56px}
.feature h3{position:absolute;left:119px;top:10px;font:700 17px var(--head);line-height:24px;color:var(--white);text-transform:uppercase}
.feature p{position:absolute;left:117px;top:66px;width:190px;font-size:13px;line-height:19px;color:var(--white)}

/* mission */
.mission-title{left:180px;top:1572px;font:800 29px var(--head);color:var(--ink)}
.mission-copy{left:181px;top:1626px;width:425px;font-size:15px;line-height:27.3px;color:#333}
.mission-deco{left:0;top:0;width:1200px;height:2270px;z-index:2;pointer-events:none}
.mission-photo{left:668px;top:1524px;width:324px;height:370px;z-index:3;
  clip-path:polygon(50% 0,100% 25%,100% 75%,50% 100%,0 75%,0 25%);
  background:linear-gradient(180deg,#6f9ed0 0%,#9cc0e2 35%,#4a6a90 65%,#8a93a0 100%)}

/* footer */
.footer{left:0;top:1878px;width:1200px;height:392px;background:var(--dark);z-index:1;color:var(--white)}
.footer-brand{position:absolute;left:181px;top:118px;width:200px;display:flex;flex-direction:column;align-items:flex-start;gap:12px}
.footer-brand .mark{width:40px;height:40px;background:var(--white)}
.footer-brand span{font:700 20px var(--head);line-height:1.2}
.foot-col{position:absolute;top:75px}
.foot-col h4{font:700 16px var(--head);margin-bottom:16px}
.foot-col ul{list-style:none;font-size:14px}
.contact-list li{display:flex;align-items:center;gap:10px;height:34px;white-space:nowrap}
.contact-list svg{width:17px;height:17px;flex:none}
.company-list li{height:28.5px;padding-left:3px}
.social-list li{display:flex;align-items:center;gap:9px;height:34px}
.social-list .dot{width:28px;height:28px;border-radius:50%;background:var(--white);display:flex;align-items:center;justify-content:center}
.social-list .dot i{width:12px;height:12px;border-radius:50%;background:var(--orange)}
.footer-rule{position:absolute;left:0;right:0;top:323px;height:1px;background:#3a2a22}
.copyright{position:absolute;left:0;right:55px;top:344px;text-align:center;font-size:15px;color:#bcb3ad}
</style>
</head>
<body>
<div class="page">

  <header>
    <div class="abs call-bar">
      <svg viewBox="0 0 24 24" fill="#fff"><path d="M6.6 10.8a15.1 15.1 0 0 0 6.6 6.6l2.2-2.2c.3-.3.7-.4 1-.2 1.1.4 2.3.6 3.6.6.6 0 1 .4 1 1V20c0 .6-.4 1-1 1A17 17 0 0 1 3 4c0-.6.4-1 1-1h3.5c.6 0 1 .4 1 1 0 1.2.2 2.4.6 3.6.1.3 0 .7-.2 1z"/></svg>
      CALL US NOW 610 555 0182
    </div>
    <div class="abs brand">
      <div class="brand-mark"></div>
      <div class="brand-name">Cobaltine Building Company</div>
    </div>
    <nav class="abs nav">
      <a style="left:0">HOME</a>
      <a class="active" style="left:80px">ABOUT US</a>
      <a style="left:192px">GALLERY</a>
      <a style="left:297px">DEPARTMENTS</a>
      <a style="left:444px">SUPPLIES</a>
      <a style="left:553px">CONTACT US</a>
    </nav>
  </header>

  <section class="abs hero">
    <div class="hero-photo" role="img" aria-label="City skyline with towers and cranes under construction"></div>
    <h1>ABOUT</h1>
    <svg viewBox="0 0 1200 428" preserveAspectRatio="none">
      <rect x="0" y="419" width="1200" height="9" fill="var(--orange)"/>
      <polygon points="360,420 596,329 840,420 826,428 372,428" fill="var(--orange)"/>
      <polygon points="376,428 596,348 822,428" fill="#fff"/>
    </svg>
  </section>

  <section class="about">
    <div class="abs about-frame" style="left:441px;top:634px;width:87px;height:7px"></div>
    <div class="abs about-frame" style="left:521px;top:634px;width:7px;height:115px"></div>
    <div class="abs about-frame" style="left:153px;top:853px;width:7px;height:127px"></div>
    <div class="abs about-frame" style="left:153px;top:973px;width:86px;height:7px"></div>
    <div class="abs about-photo" role="img" aria-label="Night aerial view of the city with a landmark tower"></div>
    <h2 class="abs about-title">ABOUT US</h2>
    <div class="abs about-copy">
      <p>CBC (Previously Al-Noura) was established in the year 1980 as a sub-contractor Specialized in waterproofing and specialized finishing, with the main target of furnishing the Saudi market by a professional team of engineers and applicators to abide by the need of the fast-growing construtiion world in the Kingdom.</p>
      <p>Nunc tempus felis vitae urna Vivamus porttitor neque at volutpat rutrum purus nisi eleifend libero a tempus libero lectus feugiat felis Morbi diam mauris viverra in gravida eu mattis in ante Morbi eget arcu Morbi porta libero id ullamcorper nonum</p>
    </div>
  </section>

  <section class="abs why">
    <svg width="1200" height="425" viewBox="0 0 1200 425" style="position:absolute;inset:0">
      <defs>
        <linearGradient id="whyFill" x1="0" y1="0" x2="0" y2="1">
          <stop offset="0" stop-color="#3a2716"/>
          <stop offset="0.45" stop-color="#6a4418"/>
          <stop offset="1" stop-color="#f0a020"/>
        </linearGradient>
      </defs>
      <path d="M0 62 L590 0 L1200 62 L1200 361 L590 423 L0 361 Z" fill="url(#whyFill)"/>
      <path d="M0 360 L590 421 L1200 360" fill="none" stroke="#2e1f12" stroke-width="6"/>
    </svg>
    <h2>WHY CHOOSE US</h2>
    <div class="feature" style="left:163px">
      <div class="hex"><svg viewBox="0 0 56 56" fill="none" stroke="#fff" stroke-width="2"><path d="M12 30a16 16 0 0 1 32 0"/><path d="M8 30h40v5H8z"/><path d="M28 14v8"/><path d="M14 46h28"/></svg></div>
      <h3>Experienced<br>Engineer</h3>
      <p>Pellentesque faucibus Ut accum san ultricies elit</p>
    </div>
    <div class="feature" style="left:474px">
      <div class="hex"><svg viewBox="0 0 56 56" fill="none" stroke="#fff" stroke-width="2"><rect x="24" y="8" width="14" height="40"/><rect x="12" y="24" width="12" height="24"/><path d="M28 14h6M28 20h6M28 26h6M28 32h6M28 38h6M16 30h4M16 36h4M16 42h4M6 48h44"/></svg></div>
      <h3>Excellent<br>Service</h3>
      <p>Pellentesque faucibus Ut accum san ultricies elit</p>
    </div>
    <div class="feature" style="left:783px">
      <div class="hex"><svg viewBox="0 0 56 56" fill="none" stroke="#fff" stroke-width="2"><circle cx="28" cy="22" r="13"/><circle cx="28" cy="22" r="9"/><path d="M28 16l2 4 4 .5-3 3 .8 4-3.8-2-3.8 2 .8-4-3-3 4-.5z"/><path d="M19 32l-6 14 6-2 3 5 5-14M37 32l6 14-6-2-3 5-5-14"/></svg></div>
      <h3>High Quality<br>Work</h3>
      <p>Pellentesque faucibus Ut accum san ultricies elit</p>
    </div>
  </section>

  <section class="mission">
    <h2 class="abs mission-title">OUR MISSION</h2>
    <p class="abs mission-copy">Maecenas aliquet velit vel turpis Mauris neque metus malesuada nec ultricies sit amet porttitor mattis enim In massa libero interdum nec interdum vel blandit sed nulla In ullamcorper est eget tempor cursus neque mi consectetuer mi a ultricies massa est sed nisl Class aptent taciti sociosqu ad litora torquent per conubia nostra per inceptos hymenaeos Proin nulla</p>
    <svg class="abs mission-deco" viewBox="0 0 1200 2270">
      <polygon points="760,1878 898,1878 829,1916" fill="#fff"/>
      <polygon points="733,1560 829,1506 927,1560" fill="var(--orange)"/>
      <polygon points="720,1836 940,1836 829,1901" fill="var(--orange)"/>
    </svg>
    <div class="abs mission-photo" role="img" aria-label="Modern glass towers and cranes against a blue sky"></div>
  </section>

  <footer class="abs footer">
    <div class="footer-brand"><div class="mark"></div><span>Cobaltine<br>Building<br>Company</span></div>
    <div class="foot-col" style="left:444px">
      <h4>CONTACT US</h4>
      <ul class="contact-list">
        <li><svg viewBox="0 0 24 24" fill="none" stroke="#fff" stroke-width="1.6"><path d="M12 22s7-7 7-12a7 7 0 0 0-14 0c0 5 7 12 7 12z"/><circle cx="12" cy="10" r="2.5"/></svg>P.O.Box.4410 Riyadh 11520 K.S.A</li>
        <li><svg viewBox="0 0 24 24" fill="none" stroke="#fff" stroke-width="1.6"><path d="M5 3h4l2 5-2.5 1.5a11 11 0 0 0 6 6L16 13l5 2v4a2 2 0 0 1-2 2A17 17 0 0 1 3 5a2 2 0 0 1 2-2z"/></svg>+966 11 5550147</li>
        <li><svg viewBox="0 0 24 24" fill="none" stroke="#fff" stroke-width="1.6"><rect x="4" y="8" width="16" height="13" rx="1"/><path d="M7 8V3h10v5M8 12h2M11 12h2M14 12h2M8 15h2M11 15h2M14 15h2"/></svg>+966 11 5550263</li>
        <li><svg viewBox="0 0 24 24" fill="none" stroke="#fff" stroke-width="1.6"><rect x="3" y="6" width="18" height="12"/><path d="M3 6l9 7 9-7"/></svg>hello@cobaltine-build.example</li>
      </ul>
    </div>
    <div class="foot-col" style="left:736px">
      <h4>COMPANY</h4>
      <ul class="company-list">
        <li>About us</li><li>Gallery</li><li>Divisions</li><li>Supplies</li><li>Contact us</li>
      </ul>
    </div>
    <div class="foot-col" style="left:902px">
      <h4>GET IN TOUCH</h4>
      <ul class="social-list">
        <li><span class="dot"><i></i></span>Chirper</li>
        <li><span class="dot"><i></i></span>Facepage</li>
        <li><span class="dot"><i></i></span>Linkwork</li>
        <li><span class="dot"><i></i></span>Pictura</li>
      </ul>
    </div>
    <div class="footer-rule"></div>
    <p class="copyright">Copyright © 2019 All right reserved</p>
  </footer>

</div>
</body>
</html>
```